Occupational Medical Billing and Coding Business needs Postcard

Medical billing and coding business needs marketing postcard to send to target audience of orthopaedic surgeons who practice medicine in California Workers' Compensation industry. These doctors treat injured workers and/or provide medical-legal evaluations and reports for the courts to settle the injured worker's claim. This is a highly specialized area of medical billing and coding. It is extremely complicated and can be very frustrating for doctors and their staff who do not understand the system. I would encourage the designers to check out my website: www.CorvaleHealthClaims.com
I want something bright and colorful that makes bold statements. It has to get their attention. My suggestions for bold statements include:
1) QMEs! Are your bills compliant with DWC's view? We make sure your complexity factors are maximized as well as compliant.
2) We collected over $ 462,000 just in second bill review (SBR) appeals alone and that's just one orthopaedic surgeon! Imagine what we can do for you!

I uploaded a word document with some information about the services I offer. The company logo is also there. Let me know if you need it in another format. The items with the asterisk (**) must be in the postcard.

Thank you so much!

Corvale Health Claims

Target Market(s)

Orthopaedic Surgeons who treat injured workers in California

Font styles to use
Sans Serif

Colors

Designer to choose colors to be used in the design.

Requirements
Must have
• Expert Billing and Coding Services for:
• QME - AME - IME Evaluations
• Radiology - MRI/CT Scans
• Orthopaedic Surgery
• Certified Coders on Staff
• Electronic Claim Submission
• Payment within 15 days
• It's important to spell orthopaedic with the "A" after the "P" as it is an acknowledgment of the origins of the practice and will attract a doctor with higher education.

```html
<!DOCTYPE html>
<html lang="en">
<head>
<meta charset="utf-8">
<title>Corvale Health Claims – Postcard</title>
<link rel="stylesheet" href="https://fonts.googleapis.com/css2?family=Cinzel:wght@400;700&family=Lato:ital,wght@0,400;0,700;0,900;1,400;1,700&family=Montserrat:wght@700;800&display=swap">
<style>
:root{
  --stage:#3b3b3b;
  --paper:#ffffff;
  --blue:#3a8fd0;
  --blue-light:#63aee2;
  --blue-deep:#1f6fb2;
  --navy:#1f3346;
  --ink:#2a2a2a;
  --charcoal:#2f2f31;
  --text:#333;
}
*{box-sizing:border-box;margin:0;padding:0}
html,body{width:902px;height:1200px;overflow:hidden}
body{background:var(--stage);position:relative;font-family:"Lato",sans-serif;color:var(--text)}

.card-slot{position:absolute}
.card-slot.front-slot{left:67px;top:20px;width:767px;height:562px}
.card-slot.back-slot{left:77px;top:602px;width:747px;height:577px}
.card{position:absolute;left:0;top:0;background:var(--paper);transform-origin:0 0;transform:scale(1.22);overflow:hidden;box-shadow:0 6px 18px rgba(0,0,0,.45)}
.card-front{width:629px;height:461px}
.card-back{width:612px;height:473px}
.shapes{position:absolute;left:0;top:0}

/* front */
.brand{position:absolute;left:48px;top:38px;width:240px;font-family:"Lato",sans-serif;font-weight:400;font-size:27px;line-height:1.1;color:var(--ink);text-align:center}
.headline{position:absolute;left:20px;top:132px;width:320px;color:#fff}
.headline .qme{font-family:"Lato",sans-serif;font-weight:900;font-size:35px;line-height:1}
.headline .question{font-family:"Cinzel",serif;font-size:16px;line-height:1.15;margin-top:8px;letter-spacing:.3px}
.headline .promise{font-family:"Montserrat",sans-serif;font-weight:800;font-size:14px;line-height:1.4;color:var(--navy);margin-top:8px;letter-spacing:.2px}
.services{position:absolute;left:20px;top:302px;width:300px}
.services h2{font-family:"Cinzel",serif;font-weight:700;font-size:13px;line-height:1.1;color:var(--blue-deep)}
.service-cols{display:flex;gap:6px;margin-top:10px}
.service-cols ul{list-style:none;font-style:italic;font-size:9.6px;line-height:1.2;color:var(--ink)}
.service-cols ul:first-child{width:150px}
.service-cols ul:last-child{width:130px}
.service-cols li{position:relative;padding-left:13px;margin-bottom:6px}
.service-cols li::before{content:"";position:absolute;left:0;top:3px;width:6px;height:6px;border-radius:50%;background:var(--blue)}
.proof{position:absolute;left:330px;top:294px;width:292px;color:#fff;font-size:13.5px;line-height:1.25}
.proof .imagine{font-weight:700;font-size:18px;color:var(--ink);margin-top:8px}
.contact-front{position:absolute;right:16px;bottom:6px;text-align:right;color:#fff;font-weight:700;font-size:11px;line-height:1.4;white-space:nowrap}
.contact-front .call{font-size:12px;letter-spacing:.4px;line-height:1.3}
.contact-front .call b{font-size:19px;font-weight:900;margin-left:4px}
.contact-front .label{color:var(--blue-light)}

/* back */
.collect{position:absolute;left:0;top:192px;width:295px;padding:0 12px}
.collect h2{font-family:"Cinzel",serif;font-weight:700;font-size:11px;line-height:1.15;text-align:center;color:var(--ink)}
.collect p{font-size:10px;line-height:1.3;text-align:justify;margin-top:8px;color:var(--ink)}
.collect .lead{color:var(--blue-deep)}
.contact-back{position:absolute;left:0;top:341px;width:295px;height:54px;background:var(--charcoal);color:#fff;font-weight:700;font-size:9.5px;padding:5px 0 0 22px;line-height:1.42}
.contact-back li{list-style:none;display:flex;align-items:center;gap:7px}
.contact-back svg{width:10px;height:10px;flex:none}
.divider{position:absolute;left:295px;top:0;width:8px;height:473px;background:linear-gradient(90deg,rgba(0,0,0,.18),rgba(0,0,0,0))}
.brand-small{position:absolute;left:322px;top:26px;font-family:"Lato",sans-serif;font-weight:400;font-size:12px;line-height:1.1;color:var(--ink);white-space:nowrap}
.stamp-box{position:absolute;left:490px;top:32px;width:86px;height:88px;border:1.5px solid #b9b9b9}
.address-line{position:absolute;left:355px;width:221px;height:1px;background:#444}
</style>
</head>
<body>

<div class="card-slot front-slot">
  <article class="card card-front">
    <svg class="shapes" width="629" height="461" viewBox="0 0 629 461">
      <defs>
        <linearGradient id="bandBlue" x1="0" y1="0" x2="1" y2="1">
          <stop offset="0" stop-color="#2c82c6"/>
          <stop offset="1" stop-color="#62aee2"/>
        </linearGradient>
        <linearGradient id="photoTone" x1="0" y1="0" x2="1" y2="1">
          <stop offset="0" stop-color="#eef2f6"/>
          <stop offset=".6" stop-color="#c9d5e1"/>
          <stop offset="1" stop-color="#8fa8c0"/>
        </linearGradient>
      </defs>
      <path d="M0 128 H362 C348 170 338 230 346 290 H0 Z" fill="url(#bandBlue)"/>
      <g role="img" aria-label="Photo of a stethoscope lying on a medical billing statement">
        <path d="M370 0 H629 V262 C560 250 430 256 330 286 C344 200 334 140 368 100 C384 70 376 30 370 0 Z" fill="url(#photoTone)"/>
      </g>
      <path d="M370 0 C376 30 384 70 368 100 C334 140 344 200 330 286" fill="none" stroke="#3a8fd0" stroke-width="7"/>
      <path d="M318 292 C430 258 560 252 629 262 V384 C520 378 420 392 330 432 C316 400 314 340 318 292 Z" fill="#3a8fd0"/>
      <path d="M270 461 C360 408 490 390 629 392 V461 Z" fill="#2f2f31"/>
    </svg>

    <div class="brand">Corvale Health Claims</div>

    <div class="headline">
      <p class="qme">QMEs!</p>
      <p class="question">Are your bills compliant with DWC's view?</p>
      <p class="promise">WE MAKE SURE YOUR COMPLEXITY FACTORS ARE MAXIMIZED AS WELL AS COMPLIANT</p>
    </div>

    <section class="services">
      <h2>Expert Billing and Coding<br>Services for:</h2>
      <div class="service-cols">
        <ul>
          <li>QME – AME – IME Evaluations</li>
          <li>Radiology – MRI/CT Scans</li>
          <li>Electrodiagnostic Studies</li>
          <li>Orthopaedic Surgery</li>
          <li>Ambulatory Surgery Centers</li>
          <li>Treatment – Primary/Secondary Physician</li>
        </ul>
        <ul>
          <li>Certified Coders on Staff</li>
          <li>Electronic Claim Submission</li>
          <li>Payment within 15 days</li>
          <li>Over 25 Years Experience in Workers' Comp</li>
        </ul>
      </div>
    </section>

    <div class="proof">
      <p>We collected over $ 462,000 just in second bill review (SBR) appeals alone and that's just one orthopaedic surgeon!</p>
      <p class="imagine">Imagine what we can do for you!</p>
    </div>

    <div class="contact-front">
      <p class="call">CALL US TODAY:<b>714. 555.0184</b></p>
      <p><span class="label">Send us an eMail:</span> info@CorvaleHealthClaims.com</p>
      <p><span class="label">Visit our Website</span> : www.CorvaleHealthClaims.com</p>
    </div>
  </article>
</div>

<div class="card-slot back-slot">
  <article class="card card-back">
    <svg class="shapes" width="612" height="473" viewBox="0 0 612 473">
      <defs>
        <linearGradient id="backPhoto" x1="0" y1="0" x2="1" y2="1">
          <stop offset="0" stop-color="#2a73b8"/>
          <stop offset=".5" stop-color="#8fb3d4"/>
          <stop offset="1" stop-color="#1c5a96"/>
        </linearGradient>
      </defs>
      <g role="img" aria-label="Photo of a calculator and stethoscope on paperwork">
        <path d="M0 0 H295 V202 C210 178 90 176 0 190 Z" fill="url(#backPhoto)"/>
      </g>
      <path d="M0 190 C90 176 210 178 295 202" fill="none" stroke="#3a8fd0" stroke-width="3"/>
    </svg>

    <section class="collect">
      <h2>We also provide<br>collection services:</h2>
      <p><span class="lead">Expert Denial Management:</span> Timely filing of SBR and IBR Appeals- Collected over $462,000 just in second bill review appeals. This is an example of ONE orthopaedic surgeon to date. Imagine what we can do for you!</p>
      <p>Don't let insurance companies "zero-out" your QME and AME bills. We get your medical-legal bills paid including penalty, interest and costs associated with the effort to collect.</p>
    </section>

    <ul class="contact-back">
      <li><svg viewBox="0 0 10 10"><circle cx="5" cy="5" r="4.4" fill="none" stroke="#fff" stroke-width=".9"/><path d="M3.4 2.8 L4.2 2.6 L4.6 3.8 L4.1 4.2 C4.4 4.9 5 5.5 5.7 5.8 L6.1 5.3 L7.3 5.7 L7.1 6.5 C5.4 6.7 3.3 4.6 3.4 2.8 Z" fill="#fff"/></svg>714. 555.0184</li>
      <li><svg viewBox="0 0 10 10"><rect x="1" y="2.5" width="8" height="5.5" fill="#fff"/><path d="M1 2.5 L5 5.6 L9 2.5" fill="none" stroke="#2f2f31" stroke-width=".8"/></svg>info@CorvaleHealthClaims.com</li>
      <li><svg viewBox="0 0 10 10"><g fill="none" stroke="#fff" stroke-width=".8"><circle cx="5" cy="5" r="4"/><ellipse cx="5" cy="5" rx="1.8" ry="4"/><path d="M1 5 H9 M1.7 3 H8.3 M1.7 7 H8.3"/></g></svg>www.corvalehealthclaims.com</li>
    </ul>

    <div class="divider"></div>
    <div class="brand-small">Corvale Health Claims</div>
    <div class="stamp-box"></div>
    <div class="address-line" style="top:210px"></div>
    <div class="address-line" style="top:272px"></div>
    <div class="address-line" style="top:333px"></div>
  </article>
</div>

</body>
</html>
```